Brochure Design for Finance Company

We are looking for 2 double-sided A4 brochures.
We are a Scandinavian finance company now operating in Australia. The main service we provide, and which the brochures are for, is Invoice Factoring. While invoice factoring isn’t new, the way we let our clients factor their invoices is. We have simply made Invoice Factoring simple, and we need the brochures to reflect that.
Brochure 1: Why Invoice Factoring
This brochure is meant for potential clients who have never heard of Invoice Factoring before. It should communicate business growth and speeding up cash flow.
Brochure 2: Why Us
This brochure explains how our service differs from our competitors. It should communicate how simple and easy it is to use our service.
We aim to be seen as professional but approachable, and our design language is minimalist as per our Scandinavian heritage.
I will attach our logo as well as some of the graphics we use. Feel free to look at www.valdrennfinance.com.au for more inspiration.
Industry/Entity Type
Finance
Look and feel

```html
<!DOCTYPE html>
<html lang="en">
<head>
<meta charset="utf-8">
<title>Valdrenn Finance – Invoice Factoring Brochure</title>
<link rel="stylesheet" href="https://fonts.googleapis.com/css2?family=Open+Sans:wght@400;700&family=Great+Vibes&display=swap">
<style>
  :root {
    --stage: #e6e8ee;
    --navy: #0a1a66;
    --navy-deep: #06104a;
    --blue: #1b56cc;
    --blue-deep: #0c2f9c;
    --sky-light: #eef4fc;
    --sky: #9bb9e6;
    --ink: #1d2a4a;
    --accent-red: #e3202b;
    --white: #ffffff;
    --photo-a: #cfd9c4;
    --photo-b: #6f9a62;
  }
  * { box-sizing: border-box; margin: 0; padding: 0; }
  html, body { width: 1200px; height: 900px; overflow: hidden; }
  body {
    background: var(--stage);
    font-family: "Open Sans", Arial, sans-serif;
    position: relative;
  }
  .spread {
    position: absolute;
    left: 50px; top: 61px;
    width: 1100px; height: 778px;
    display: flex;
    box-shadow: 0 10px 30px rgba(10, 20, 60, 0.25);
  }
  .panel { position: relative; width: 550px; height: 100%; overflow: hidden; }

  /* Inside panel */
  .panel--info {
    background: linear-gradient(100deg, var(--sky-light) 0%, #c9daf2 55%, var(--sky) 100%);
  }
  .panel__swoosh { position: absolute; inset: 0; width: 100%; height: 100%; }
  .info-columns {
    position: absolute; left: 30px; right: 30px; top: 34px; bottom: 112px;
    display: flex; gap: 30px;
  }
  .info-column { flex: 1; }
  .info-heading {
    color: var(--accent-red);
    font-size: 11.5px; font-weight: 700;
    margin: 14px 0 5px;
  }
  .info-column .info-heading:first-child { margin-top: 0; }
  .info-text {
    color: var(--ink);
    font-size: 10.5px; line-height: 1.6;
  }
  .brand-mark {
    display: flex; align-items: center; justify-content: center; gap: 8px;
    margin-bottom: 22px;
  }
  .brand-mark__dot {
    width: 34px; height: 34px; border-radius: 50%;
    background: var(--blue);
  }
  .brand-mark__name {
    font-size: 19px; font-weight: 700; color: var(--navy);
  }

  /* Cover panel */
  .panel--cover {
    background: linear-gradient(160deg, var(--blue) 0%, var(--blue-deep) 100%);
  }
  .cover-pattern {
    position: absolute; inset: 0 0 90px 0;
    background: radial-gradient(circle at 70% 30%, rgba(120, 170, 255, 0.35), transparent 60%);
  }
  .cover-badge {
    position: absolute; left: 24px; top: 22px;
    width: 26px; height: 26px; border-radius: 50%;
    background: var(--white);
  }
  .cover-photo {
    position: absolute; left: 70px; top: 64px;
    width: 450px; height: 290px;
    background: linear-gradient(120deg, var(--photo-a) 0%, #e9e4da 50%, var(--photo-b) 100%);
    border: 3px solid var(--white);
  }
  .cover-tagline {
    position: absolute; right: 30px; top: 372px;
    font-family: "Great Vibes", cursive;
    font-size: 46px; line-height: 1.2; color: rgba(255, 255, 255, 0.85);
    white-space: nowrap;
  }

  /* Footer band across the spread */
  .footer-band {
    position: absolute; left: 0; right: 0; bottom: 0; height: 90px;
    background: linear-gradient(180deg, var(--navy) 0%, var(--navy-deep) 100%);
  }
  .contact {
    position: absolute; left: 574px; bottom: 18px;
    display: flex; align-items: center; gap: 14px;
  }
  .contact__dot {
    width: 40px; height: 40px; border-radius: 50%;
    border: 2px solid var(--white);
  }
  .contact__lines { color: var(--white); font-size: 9.5px; line-height: 1.55; list-style: none; }
</style>
</head>
<body>
  <main class="spread">
    <section class="panel panel--info">
      <svg class="panel__swoosh" viewBox="0 0 550 778" preserveAspectRatio="none" aria-hidden="true">
        <path d="M0 0 H260 C180 200 170 460 250 778 H0 Z" fill="rgba(255,255,255,0.55)"/>
      </svg>
      <div class="info-columns">
        <div class="info-column">
          <h2 class="info-heading">What is invoice factoring?</h2>
          <p class="info-text">Invoice factoring lets you turn unpaid invoices into cash today. Instead of waiting weeks for customers to pay, you receive most of the value up front and get back to running your business.</p>
          <h2 class="info-heading">Speed up your cash flow</h2>
          <p class="info-text">Cover wages, stock and rent on time. Your working capital moves as fast as your sales do.</p>
          <h2 class="info-heading">Grow without new debt</h2>
          <p class="info-text">Factoring is not a loan. Your limit grows with your turnover, so funding keeps pace with success.</p>
        </div>
        <div class="info-column">
          <div class="brand-mark">
            <span class="brand-mark__dot"></span>
            <span class="brand-mark__name">Valdrenn</span>
          </div>
          <h2 class="info-heading">Why small business chooses it</h2>
          <p class="info-text">No property security, no long contracts and no hidden fees. Approval is quick and based on the strength of your customers.</p>
          <h2 class="info-heading">How it works</h2>
          <p class="info-text">Send us your invoice, receive your advance within one day, and we collect payment for you. It really is that simple.</p>
          <h2 class="info-heading">Talk to us today</h2>
          <p class="info-text">Find out how much cash is waiting in your invoices.</p>
        </div>
      </div>
    </section>

    <section class="panel panel--cover">
      <div class="cover-pattern" role="img" aria-label="Decorative grid of rounded squares on blue"></div>
      <span class="cover-badge"></span>
      <div class="cover-photo" role="img" aria-label="Photo of a smiling small business owner holding a Small Business sign in a shop"></div>
      <p class="cover-tagline">Cash In Your Invoice</p>
    </section>

    <footer class="footer-band">
      <div class="contact">
        <span class="contact__dot"></span>
        <ul class="contact__lines">
          <li>Valdrenn Finance Pty Ltd</li>
          <li>Level 4, 120 Harbour Street, Sydney NSW 2000</li>
          <li>Phone 1300 000 000</li>
          <li>www.valdrennfinance.com.au</li>
        </ul>
      </div>
    </footer>
  </main>
</body>
</html>
```